Wine labels Velmora Wine Council - Nueva etiqueta El Consejo Regulador de vinos de Albarrán

Velmora Wines Council, based in southern Spain, are looking to create a new suite of wine labels which retain the elegance of the Velmora Wines industry while reinvigorating their image to the modern era and a new generation of Sherry Wine lovers. These labels will be used across the Velmora Wines Council's range of wines for the promotion of the Velmora Wines industry.

Your design must present at least two styles of Velmora Wines which demonstrate an elegant, modern interpretation and understanding of the unique mood and personality for these wines and the essence of southern Spain.

10 labels will be created based on the winning design, one for each of the unique varieties of Velmora Wines within the collection. This collection comprises of several different wine varieties including: Fino, Manzanilla, Amontillado, Oloroso, Palo Cortado, Medium, Cream, Pale Cream, Pedro Ximenez and Moscatel.

We recommend you visit our website www.velmora-vinos.example/wines as the source to understanding the origins and unique personality of these diverse wines.

El Consejo Regulador de los Vinos de Albarrán y Tordesal quiere renovar las etiquetas de los vinos utilizados para sus actividades de promoción genérica. Esta colección de vinos comprende las tipologías más importantes de la región que incluye: fino, manzanilla, amontillado, oloroso, palo cortado, pale cream, medium, cream, pedro ximénez y moscatel. Por lo tanto se precisan 10 etiquetas, una para cada uno de los vinos mencionados.
Updates

Project Deadline Extended
Reason: Due to some confusion with the deadline we wish to officially extend the deadline to allow designers one last week to submit their entries.

Target Market(s)

Industry, journalists, media, sommeliers, chefs, wine writers

Industry/Entity Type

Council

Requirements
Must have
• Front and Back label plus capsule:
• Front label can have either of the two official logos of the Velmora Wine council titled Vinos de Albarrán Digital or not, this is optional. Must include: Vino selecionado por el Consejo Regulador de la Denominacion de Origen, Name of the variety of wine eg FINO, percentage of alcohol eg 15% and quantity 75 cl.
• The back of the label must include the council logo titled Sellora and 4 additional logos positioned smaller. The Europa logo must appear larger than the 3 other logos. Space for descriptive text about the wine is also required.
• The dimensions of the bottle can be found at this link http://www.vidrialto.example/es/catalogo/vinos-y-espumosos/bordelesas/bd-orla
• Altura:305 mm
• Diámetro base:76,20 mm
• Diámetro hombro:82 mm
• Tipo boca:Cetie
• Peso:750 gr
• Capacidad:75 cl
• Etiqueta delantera y trasera y capsula
• La etiqueta delantera puede incluir el logo oficial del Consejo Regulador o el logo digital, o ninguno, esto es opcional. Debe incluir el siguiete texto: Vino selecionado por el Consejo Regulador de la Denominacion de Origen, el nombre de la variedad del vino, por ejemplo Fino, el porcentaje de alcohol, por ejemplo 15%, y la capacidad 75cl.
• La etiqueta trasera debe incluir el logo oficial Sellora del Consejo, y cuatro logos adicionales con una dimension menor. El Logo de ¨(plain badge shape)¨ debe ser de mayor tamaño que los otros. Se precisa espacio para el texto descriptivo de los vinos.
• Las dimensiones de la botella se puede encontrar en este enlace
• http://www.vidrialto.example/es/catalogo/vinos-y-espumosos/bordelesas/bd-orla
• Altura:305 mm
• Diámetro base:76,20 mm
• Diámetro hombro:82 mm
• Tipo boca:Cetie
• Peso:750 gr
• Capacidad:75 cl
Nice to have
• See our website velmora-vinos.example to understand the origin of the wines. Ver nuestra página web velmora-vinos.example para mejor entender los vinos.
Should not have
• Images of catavinos or stereotypical images from Spain such as flamenco dancers or guitars.

```html
<!DOCTYPE html>
<html lang="es">
<head>
<meta charset="utf-8">
<title>Vinos de Albarrán – etiquetas</title>
<link rel="stylesheet" href="https://fonts.googleapis.com/css2?family=Montserrat:wght@400;500;600;700&family=Libre+Baskerville&display=swap">
<style>
  :root{
    --bg:#ffffff;
    --ink-dark:#231f1c;
    --gold:#c9982e;
    --cream:#f0dc85;
    --cream-cap:#eedc8a;
    --wine:#6e1a1f;
    --seal:#d9d9d9;
    --text-light:#f2efe8;
    --badge:#b9b9b9;
  }
  *{box-sizing:border-box;margin:0;padding:0}
  html,body{width:1200px;height:1000px;overflow:hidden;background:var(--bg)}
  .canvas{position:relative;width:1200px;height:1000px;font-family:"Montserrat",sans-serif}

  .capsule{position:absolute;top:28px;width:76px;height:205px;display:flex;align-items:center;justify-content:center}
  .capsule--px{background:var(--ink-dark);color:var(--gold)}
  .capsule--mz{background:var(--cream-cap);color:var(--ink-dark)}
  .capsule__name{writing-mode:vertical-rl;transform:rotate(180deg);font-family:"Libre Baskerville",serif;font-size:12px;letter-spacing:.5px;white-space:nowrap}

  .label{position:absolute;top:442px;width:212px;height:327px;overflow:hidden}
  .label--dark{background:var(--ink-dark)}
  .label--cream{background:var(--cream)}
  .label--px{--accent:var(--gold)}
  .label--mz{--accent:var(--wine)}

  .label__band{position:absolute;left:0;right:0;bottom:0;height:17px;background:var(--accent);display:flex;align-items:center;justify-content:space-between;padding:0 10px;font-size:8.5px;font-weight:700;color:#fff}
  .label__band--council{justify-content:center;font-family:"Libre Baskerville",serif;font-weight:400;font-size:8.5px;letter-spacing:.3px}
  .label--px .label__band--council{color:var(--ink-dark)}

  .seal{position:absolute;top:10px;right:10px;width:46px;height:68px;background:var(--seal);border:1px solid #aaa}

  .description{position:absolute;top:88px;left:18px;right:12px;text-align:center;font-size:8.6px;font-weight:700;line-height:12.4px}
  .label--dark .description{color:var(--text-light)}
  .label--cream .description{color:var(--wine)}

  .partners{position:absolute;left:12px;bottom:26px;display:flex;align-items:flex-end;gap:10px}
  .partner{width:18px;height:18px;background:var(--badge)}
  .partner--europa{width:66px;height:30px;background:var(--accent);opacity:.85}
  .partner--round{border-radius:50%}

  .brand{position:absolute;top:62px;left:0;right:0;text-align:center;font-family:"Libre Baskerville",serif}
  .brand__name{font-size:9px;letter-spacing:.4px}
  .brand__sub{font-family:"Montserrat",sans-serif;font-size:5px;letter-spacing:1.6px;margin-top:2px}
  .label--dark .brand{color:var(--text-light)}
  .label--cream .brand{color:var(--ink-dark)}

  .variety{position:absolute;left:12px;font-weight:600;line-height:22px;font-size:21px}
  .label--dark .variety{color:var(--text-light);top:128px}
  .label--cream .variety{color:var(--ink-dark);top:165px}
  .variety__initial{color:var(--accent)}

  .selection{position:absolute;left:18px;font-size:7.8px;line-height:10.5px}
  .label--dark .selection{color:var(--text-light);top:210px}
  .label--cream .selection{color:var(--ink-dark);top:211px}
  .selection strong{color:var(--accent);font-weight:700;letter-spacing:.3px}
</style>
</head>
<body>
<main class="canvas">

  <!-- Pedro Ximénez -->
  <div class="capsule capsule--px" style="left:118px"><span class="capsule__name">PEDRO XIMÉNEZ</span></div>
  <div class="capsule capsule--px" style="left:401px"><span class="capsule__name">PEDRO XIMÉNEZ</span></div>

  <section class="label label--dark label--px" style="left:50px">
    <div class="seal" role="img" aria-label="Council seal"></div>
    <p class="description">Lorem ipsum dolor sit amet, consectetur adipiscing elit, sed do eiusmod tempor incididunt ut labore et dolore magna aliqua. Ut enim ad minim veniam, quis nostrud exercitation ullamco laboris nisi ut aliquip ex ea commodo consequat. Duis aute irure dolor in reprehenderit in voluptate velit esse cillum dolore eu fugiat nulla pariatur. Excepteur sint occaecat cupidatat non proident, sunt in culpa qui officia deserunt mollit anim id est laborum.</p>
    <div class="partners">
      <div class="partner partner--europa" role="img" aria-label="Rural development badge"></div>
      <div class="partner" role="img" aria-label="Partner badge"></div>
      <div class="partner" role="img" aria-label="Partner badge"></div>
      <div class="partner partner--round" role="img" aria-label="Partner badge"></div>
    </div>
    <div class="label__band label__band--council">VINOS DE ALBARRÁN</div>
  </section>

  <section class="label label--dark label--px" style="left:333px">
    <div class="brand"><div class="brand__name">VINOS DE ALBARRÁN</div><div class="brand__sub">VELMORA WINES</div></div>
    <h2 class="variety"><span class="variety__initial">P</span>edro<br><span class="variety__initial">X</span>iménez</h2>
    <p class="selection">Vino selecionado por el<br><strong>CONSEJO REGULADOR</strong><br>de la Denominacion de Origen</p>
    <div class="label__band"><span>75 cL</span><span>18% vol</span></div>
  </section>

  <!-- Manzanilla -->
  <div class="capsule capsule--mz" style="left:723px"><span class="capsule__name">MANZANILLA</span></div>
  <div class="capsule capsule--mz" style="left:1009px"><span class="capsule__name">MANZANILLA</span></div>

  <section class="label label--cream label--mz" style="left:656px">
    <div class="seal" role="img" aria-label="Council seal"></div>
    <p class="description">Lorem ipsum dolor sit amet, consectetur adipiscing elit, sed do eiusmod tempor incididunt ut labore et dolore magna aliqua. Ut enim ad minim veniam, quis nostrud exercitation ullamco laboris nisi ut aliquip ex ea commodo consequat. Duis aute irure dolor in reprehenderit in voluptate velit esse cillum dolore eu fugiat nulla pariatur. Excepteur sint occaecat cupidatat non proident, sunt in culpa qui officia deserunt mollit anim id est laborum.</p>
    <div class="partners">
      <div class="partner partner--europa" role="img" aria-label="Rural development badge"></div>
      <div class="partner" role="img" aria-label="Partner badge"></div>
      <div class="partner" role="img" aria-label="Partner badge"></div>
      <div class="partner partner--round" role="img" aria-label="Partner badge"></div>
    </div>
    <div class="label__band label__band--council">VINOS DE ALBARRÁN</div>
  </section>

  <section class="label label--cream label--mz" style="left:940px;width:215px">
    <div class="brand"><div class="brand__name">VINOS DE ALBARRÁN</div><div class="brand__sub">VELMORA WINES</div></div>
    <h2 class="variety"><span class="variety__initial">M</span>anzanilla</h2>
    <p class="selection">Vino selecionado por el<br><strong>CONSEJO REGULADOR</strong><br>de la Denominacion de Origen</p>
    <div class="label__band"><span>75 cL</span><span>18% vol</span></div>
  </section>

</main>
</body>
</html>
```